Prayer Service 12.28.2013

I need a flyer designed for a Christian prayer service. The title and theme is:
"Total and Complete Surrender for Total and Complete Deliverance!"
1. You have creative freedom with imagery and typography
2. I need a quick turnaround time
FLYER DETAILS:
A prayer, anointing, and deliverance all night prayer service, at Brookhaven Assembly.
Saturday December 28 2013 from 9pm-6am.
Special guest speakers, prayer,anointing,and deliverance sessions.
For more information contact Sis Mirela Thornbury at Brookhaven Assembly 347 562 1094 Ext. 4816 or Janelle Corbin at 631 538-2904

```html
<!DOCTYPE html>
<html lang="en">
<head>
<meta charset="utf-8">
<title>Total and Complete Surrender – All Night Prayer Service</title>
<link rel="stylesheet" href="https://fonts.googleapis.com/css2?family=Alegreya+SC:wght@400;500&family=Alegreya:ital@1&display=swap">
<style>
  :root {
    --paper: #fbfbf9;
    --damask: #ecebe7;
    --olive: #4b4a30;
    --olive-soft: #5c5b45;
    --ink: #1c1c1a;
    --rule: #6a6a5a;
  }
  html, body {
    margin: 0;
    padding: 0;
    overflow: hidden;
    background: var(--paper);
  }
  .flyer {
    position: relative;
    width: 928px;
    height: 1200px;
    overflow: hidden;
    background: radial-gradient(ellipse at 60% 45%, var(--paper) 0%, var(--damask) 100%);
    font-family: "Alegreya SC", Georgia, serif;
    color: var(--olive);
  }
  .vine-ornament {
    position: absolute;
    left: 18px;
    top: 12px;
    width: 860px;
    height: 1176px;
  }
  .title {
    position: absolute;
    width: 800px;
    margin: 0;
    text-align: center;
    font-weight: 500;
    line-height: 1;
    white-space: nowrap;
    color: var(--olive);
  }
  .title--first { left: 169px; top: 59px; font-size: 46px; }
  .title--second { left: 128px; top: 102px; font-size: 43px; }
  .subtitle {
    position: absolute;
    left: 216px;
    top: 199px;
    width: 670px;
    margin: 0;
    text-align: center;
    font-family: "Alegreya", Georgia, serif;
    font-style: italic;
    font-size: 30px;
    line-height: 42px;
    color: var(--olive-soft);
  }
  .date-badge {
    position: absolute;
    left: 326px;
    top: 322px;
    width: 490px;
    height: 280px;
  }
  .date-text {
    position: absolute;
    left: 334px;
    top: 337px;
    width: 468px;
    margin: 0;
    text-align: center;
    font-size: 36px;
    line-height: 75px;
    color: var(--olive);
  }
  .program {
    position: absolute;
    left: 390px;
    top: 626px;
    margin: 0;
    padding: 0;
    list-style: none;
    font-size: 29px;
    letter-spacing: 1.2px;
    line-height: 45.5px;
    color: var(--olive);
  }
  .program li::before {
    content: "";
    display: inline-block;
    width: 11px;
    height: 11px;
    margin-right: 16px;
    border-radius: 50%;
    background: var(--ink);
    vertical-align: 4px;
  }
  .contact-heading {
    position: absolute;
    left: 328px;
    top: 850px;
    width: 508px;
    margin: 0;
    padding-bottom: 4px;
    border-bottom: 1.5px solid var(--rule);
    font-size: 34px;
    font-weight: 400;
    line-height: 1.2;
    white-space: nowrap;
    color: var(--olive);
  }
  .contact {
    position: absolute;
    left: 247px;
    width: 660px;
    margin: 0;
    text-align: center;
    font-size: 27px;
    line-height: 46px;
    white-space: nowrap;
    color: var(--ink);
  }
  .contact--primary { top: 908px; }
  .contact--secondary { top: 1002px; line-height: 38px; }
</style>
</head>
<body>
<main class="flyer">
  <svg class="vine-ornament" viewBox="0 0 860 1176" role="img" aria-label="Black silhouette vine with leaves and rose buds climbing the left edge and trailing along the bottom">
    <defs>
      <linearGradient id="vineFade" x1="0" y1="0" x2="1" y2="0">
        <stop offset="0" stop-color="#3a3a37" stop-opacity="0.55"/>
        <stop offset="1" stop-color="#3a3a37" stop-opacity="0.08"/>
      </linearGradient>
    </defs>
    <rect x="0" y="0" width="250" height="1176" rx="20" fill="url(#vineFade)"/>
    <rect x="0" y="1080" width="860" height="96" rx="20" fill="url(#vineFade)"/>
  </svg>

  <h1 class="title title--first">Total and Complete Surrender</h1>
  <h1 class="title title--second">for Total and Complete Deliverance!</h1>

  <p class="subtitle">A prayer, anointing, and deliverance all night<br>prayer service, at Brookhaven Assembly.</p>

  <svg class="date-badge" viewBox="0 0 490 280" aria-hidden="true">
    <defs>
      <filter id="badgeShadow" x="-10%" y="-10%" width="125%" height="130%">
        <feDropShadow dx="4" dy="6" stdDeviation="5" flood-color="#000" flood-opacity="0.35"/>
      </filter>
    </defs>
    <ellipse cx="242" cy="136" rx="232" ry="124" fill="#ffffff" stroke="#1c1c1a" stroke-width="3" filter="url(#badgeShadow)"/>
  </svg>
  <p class="date-text">Saturday<br>December 28 2013<br>from 9pm-6am.</p>

  <ul class="program">
    <li>special guest speakers</li>
    <li>prayer</li>
    <li>anointing</li>
    <li>deliverance sessions</li>
  </ul>

  <h2 class="contact-heading">For more information contact:</h2>
  <p class="contact contact--primary">--- Sis Mirela Thornbury ---<br>at Brookhaven Assembly 347 562 1094 Ext. 4816</p>
  <p class="contact contact--secondary">--- or Janelle Corbin ---<br>at 631 538-2904</p>
</main>
</body>
</html>
```